Every Drawer Neatly Sorted or EDN Organized needs a business card design. EDN Organized is a professi

We need a business card design that is clean, sharp and conveys a sense of organization. I already have a logo.

Target Market(s)

Families (specifically mothers), small business owners, parents, seniors

Industry/Entity Type

Business

Contact Information for Business Card

My website is www.ednorganized-example.com and my Facebook page is http://www.socialpage-example.com/everydrawerneatlysorted. The phone number is 555-418-2706 and I want to be listed as Miriel O. Dunsford, Owner

Requirements
Must have
• My logo.

```html
<!DOCTYPE html>
<html lang="en">
<head>
<meta charset="utf-8">
<title>EDN Organized – Business Card</title>
<link rel="stylesheet" href="https://fonts.googleapis.com/css2?family=Arimo:wght@400;700&display=swap">
<style>
  :root {
    --backdrop: #3a3b3d;
    --card-black: #0b0b0c;
    --card-white: #f2f2f2;
    --brand-blue: #1e88e5;
    --ink-white: #ffffff;
    --ink-dark: #1b1b1b;
  }
  * { margin: 0; padding: 0; box-sizing: border-box; }
  html, body { width: 1200px; height: 950px; overflow: hidden; }
  body {
    background: var(--backdrop);
    font-family: "Arimo", Arial, sans-serif;
    display: flex;
    flex-direction: column;
    align-items: center;
    justify-content: center;
    gap: 50px;
  }
  .card {
    width: 700px;
    height: 400px;
    border-radius: 6px;
    position: relative;
    overflow: hidden;
    box-shadow: 0 10px 30px rgba(0,0,0,0.35);
  }
  .card--back {
    background: var(--card-white);
    display: flex;
    align-items: center;
    justify-content: center;
  }
  .card--front {
    background: var(--card-black);
    color: var(--ink-white);
  }
  .brand-mark {
    display: flex;
    align-items: center;
    gap: 14px;
    font-weight: 400;
    letter-spacing: 0.12em;
  }
  .brand-mark__dot {
    width: 16px;
    height: 16px;
    border-radius: 50%;
    background: var(--brand-blue);
  }
  .card--back .brand-mark { color: var(--ink-dark); font-size: 38px; }
  .card--front .brand-mark {
    position: absolute;
    top: 46px;
    left: 48px;
    color: var(--ink-white);
    font-size: 32px;
  }
  .contact-block {
    position: absolute;
    left: 120px;
    top: 168px;
  }
  .person-name {
    color: var(--brand-blue);
    font-weight: 700;
    font-size: 27px;
  }
  .person-role {
    font-weight: 700;
    font-size: 17px;
    margin-top: 4px;
  }
  .contact-list {
    list-style: none;
    margin-top: 36px;
    font-size: 21px;
    line-height: 1.35;
  }
  .contact-list li { display: flex; align-items: center; gap: 10px; }
  .contact-icon { width: 18px; height: 18px; flex: none; }
  .social-square {
    width: 16px; height: 16px; margin: 0 1px;
    background: var(--brand-blue); border-radius: 2px; flex: none;
  }
</style>
</head>
<body>
  <section class="card card--back" aria-label="Card back">
    <div class="brand-mark">
      <span class="brand-mark__dot"></span>
      <span class="brand-mark__name">EDN Organized</span>
    </div>
  </section>

  <section class="card card--front" aria-label="Card front">
    <div class="brand-mark">
      <span class="brand-mark__dot"></span>
      <span class="brand-mark__name">EDN Organized</span>
    </div>

    <div class="contact-block">
      <p class="person-name">Miriel O. Dunsford</p>
      <p class="person-role">Owner</p>
      <ul class="contact-list">
        <li>
          <svg class="contact-icon" viewBox="0 0 24 24" aria-hidden="true">
            <path fill="#1e88e5" d="M6.6 10.8a15.1 15.1 0 0 0 6.6 6.6l2.2-2.2a1 1 0 0 1 1-.25 11.4 11.4 0 0 0 3.6.57 1 1 0 0 1 1 1V20a1 1 0 0 1-1 1A17 17 0 0 1 3 4a1 1 0 0 1 1-1h3.5a1 1 0 0 1 1 1c0 1.25.2 2.45.57 3.57a1 1 0 0 1-.25 1z"/>
          </svg>
          <span>555-418-2706</span>
        </li>
        <li>
          <svg class="contact-icon" viewBox="0 0 24 24" aria-hidden="true">
            <circle cx="12" cy="12" r="10" fill="none" stroke="#1e88e5" stroke-width="2.4"/>
            <ellipse cx="12" cy="12" rx="4" ry="10" fill="none" stroke="#1e88e5" stroke-width="2"/>
            <line x1="2" y1="12" x2="22" y2="12" stroke="#1e88e5" stroke-width="2"/>
          </svg>
          <span>www.ednorganized-example.com</span>
        </li>
        <li>
          <span class="social-square" aria-hidden="true"></span>
          <span>everydrawerneatlysorted</span>
        </li>
      </ul>
    </div>
  </section>
</body>
</html>
```